I need a website built for my modeling agency company.

On our website, a user can create a profile and we will submit it to thousands of modeling agents throughout the country.

In many cases, they will receive multiple offers from modeling agencies which allows them to pick and choose the contract that is best for them to launch their modeling career.

Some tag lines to consider using:

"Submit your profile to hundreds of modeling agents instantly!"

"Get found and become a star!"

We are: The Runway Guild.

Our Slogan: The World''s Largest Network of Fashion Models and Agents

What We Do: We are an agency with one of the largest networks of fashion professionals that are looking for new modeling talent. We host professional profiles for aspiring models, professional fashion models seeking work, modeling talent seekers, and top modeling agencies. We connect aspiring models with the top modeling agencies in the United States and abroad.

By submitting your FREE profile, you will be instantly introduced to the industry’s leading modeling agents. Within a few days, you could receive multiple, competing offers from modeling agencies that all want to launch your modeling career. Receiving multiple signing offers puts you in control of deciding which contract best suites you!

Reason: I've seen some good designs, but none that are 100% perfect. These are the ones that I like best so far (to give you some ideas): http://files.pixelvane.example/img/510372/820114/820114_4917263_510372_image.jpg http://files.pixelvane.example/img/510372/829305/829305_4926851_510372_image.jpg http://files.pixelvane.example/img/510372/51847/51847_4924097_510372_image.jpg http://files.pixelvane.example/img/510372/51847/51847_4919856_510372_image.jpg http://files.pixelvane.example/img/510372/823670/823670_4920438_510372_image.jpg

Target Market(s)

Aspiring models (mostly female, but some male)

Industry/Entity Type

Modeling Agency

Colors

Designer to choose colors to be used in the design.

Requirements
Nice to have
• Somewhere in the top half of the page, I would like there to be a small form for the visitor to fill out. This form will look as follows:

Title: Instantly contact hundreds of modeling agents who are looking for new talent and could make you a star!
Fields: First Name*, Last Name*, Age, Zip Code, Email Address*, Daytime Phone, Evening Phone, Comments.

Then, there will be a "submit" button to proceed to next step of form. Just below the "submit" button, should be the following verbiage: "You will have the opportunity to upload photo(s) and provide other pertinent information in next step."

```html
<!DOCTYPE html>
<html lang="en">
<head>
<meta charset="utf-8">
<title>The Runway Guild — Submit Your Profile</title>
<link rel="stylesheet" href="https://fonts.googleapis.com/css2?family=Gelasio:wght@700&family=Roboto:ital,wght@0,400;1,400&display=swap">
<style>
  :root {
    --ink: #000000;
    --paper: #ffffff;
    --panel: rgba(40, 38, 36, 0.82);
    --field-text: #555555;
    --accent: #ee1c25;
    --footer-text: #c9c9c9;
    --icon: #8a8a8a;
  }
  * { box-sizing: border-box; margin: 0; padding: 0; }
  html, body { width: 1200px; height: 990px; overflow: hidden; background: var(--ink); }
  .page { position: relative; width: 1200px; height: 990px; font-family: "Roboto", Arial, sans-serif; }

  .site-header {
    position: absolute; left: 0; top: 0; width: 1200px; height: 65px;
    background: var(--ink); display: flex; justify-content: center; align-items: center;
  }
  .brand { display: flex; align-items: center; gap: 8px; color: var(--paper); }
  .brand-square { width: 26px; height: 26px; background: var(--paper); }
  .brand-text { display: flex; flex-direction: column; }
  .brand-name { font-family: "Gelasio", Georgia, serif; font-weight: 700; font-size: 20px; line-height: 22px; letter-spacing: 0.5px; }
  .brand-slogan { font-size: 6.5px; line-height: 9px; }

  .hero-photo {
    position: absolute; left: 0; top: 65px; width: 1200px; height: 887px;
    background:
      linear-gradient(180deg, rgba(0,0,0,0) 70%, rgba(20,22,30,0.5) 100%),
      linear-gradient(90deg, #6f95b4 0%, #a9c6d9 25%, #2c3550 45%, #3a3640 62%, #c9cfd2 80%, #8b96a3 100%);
  }

  .signup-panel {
    position: absolute; left: 141px; top: 440px; width: 918px; height: 427px;
    background: var(--panel);
  }
  .signup-title {
    position: absolute; left: 0; top: 34px; width: 918px; text-align: center;
    font-family: "Gelasio", Georgia, serif; font-weight: 700; font-size: 22px; line-height: 29px;
    color: var(--paper);
  }
  .signup-rule { position: absolute; left: 262px; top: 114px; width: 394px; height: 1px; background: var(--paper); }

  .field {
    position: absolute; height: 30px; background: var(--paper);
    font-style: italic; font-size: 12px; color: var(--field-text);
    padding: 8px 10px; line-height: 14px;
  }
  .field-comments { height: 143px; }
  .field-select svg { position: absolute; right: 8px; top: 11px; }

  .submit-button {
    position: absolute; left: 318px; top: 306px; width: 282px; height: 46px;
    background: var(--accent); border-radius: 6px; color: var(--paper);
    font-family: "Gelasio", Georgia, serif; font-weight: 700; font-size: 15px;
    display: flex; align-items: center; justify-content: center; gap: 10px; letter-spacing: 0.3px;
  }
  .signup-note {
    position: absolute; left: 0; top: 378px; width: 918px; text-align: center;
    font-size: 10.5px; color: var(--paper);
  }

  .site-footer {
    position: absolute; left: 0; top: 952px; width: 1200px; height: 38px; background: var(--ink);
    display: flex; justify-content: center; align-items: center; gap: 10px;
    font-size: 10px; color: var(--footer-text);
  }
  .social-links { display: flex; gap: 6px; margin-left: 4px; }
  .social-dot { width: 17px; height: 17px; border-radius: 50%; background: var(--icon); }
</style>
</head>
<body>
<div class="page">
  <header class="site-header">
    <div class="brand">
      <span class="brand-square"></span>
      <div class="brand-text">
        <span class="brand-name">The Runway Guild</span>
        <span class="brand-slogan">The World's Largest Network of Fashion Models and Agents</span>
      </div>
    </div>
  </header>

  <div class="hero-photo" role="img" aria-label="Studio fashion photograph of four models in evening dresses posing in a pale blue room"></div>

  <section class="signup-panel">
    <h1 class="signup-title">Instantly contact hundreds of modeling agents who are looking for new talent<br>and could make you a star!</h1>
    <div class="signup-rule"></div>

    <div class="field" style="left:56px;top:144px;width:197px;">First Name*</div>
    <div class="field" style="left:260px;top:144px;width:197px;">Last Name*</div>
    <div class="field field-select" style="left:56px;top:182px;width:197px;">Age
      <svg width="12" height="8" viewBox="0 0 12 8"><path d="M1 1l5 5 5-5" fill="none" stroke="#bbb" stroke-width="2"/></svg>
    </div>
    <div class="field" style="left:260px;top:182px;width:197px;">Zip Code</div>
    <div class="field" style="left:56px;top:219px;width:401px;">Email Address*</div>
    <div class="field" style="left:56px;top:257px;width:197px;">Daytime Phone</div>
    <div class="field" style="left:260px;top:257px;width:197px;">Evening Phone</div>
    <div class="field field-comments" style="left:465px;top:144px;width:401px;">Comments</div>

    <div class="submit-button">SUBMIT YOUR PROFILE
      <svg width="8" height="12" viewBox="0 0 8 12"><path d="M1.5 1.5l4.5 4.5-4.5 4.5" fill="none" stroke="#fff" stroke-width="2.4"/></svg>
    </div>
    <p class="signup-note">You will have the opportunity to upload photo(s) and provide other pertinent information in next step.</p>
  </section>

  <footer class="site-footer">
    <span>Terms of Use &nbsp;/&nbsp; ©2013 The Runway Guild.</span>
    <div class="social-links">
      <span class="social-dot"></span><span class="social-dot"></span><span class="social-dot"></span><span class="social-dot"></span>
    </div>
  </footer>
</div>
</body>
</html>
```